Accounting practice seeks business card redesign with existing logo

Accounting practice has logo and slogan but more needs modern professional business revision. Must be in a file format ready to print quality business cards.

Open to artistic ideas but for the brand recognition the features below must be incorporated:

- Logo: attached in EPS format (Logo now blue)
- Slogan: Smart Business Answers... That Deliver! (in orange legible handwriting type font)
- Name: Daniel T Hoxley BBus CA JP (letters in smaller font)
- Phone icon: 1800 531 908
- Mobile phone icon: 0412 385 714
- Web icon: www.kelnovagroup.com.au
- Email icon: admin@kelnovagroup.com.au
- See pics for dark blue/med blue line at bottom, this is a necessity.
- Globe that forms the 'dot' in the 'I' of KelNova is attached. It is too big at present.
- Rear side: pic attached. Note my logo is a watermark. I Will provide slightly revised wording details later. Please allow for a small white space at bottom of rear of card to write notes/appointment details.

I am open to ideas but must retain the above for brand recognition.

```html
<!DOCTYPE html>
<html lang="en">
<head>
<meta charset="utf-8">
<title>KelNova Solutions – Business Card</title>
<link rel="stylesheet" href="https://fonts.googleapis.com/css2?family=Roboto+Condensed:wght@300;400&family=Roboto:wght@300;400&family=Kalam:wght@300&display=swap">
<style>
  :root {
    --navy: #1b2857;
    --brand-blue: #1478c0;
    --sky: #4fa3dc;
    --ink: #3a3a3a;
    --icon: #1b2857;
    --slogan: #e8692a;
    --paper: #ffffff;
  }
  html, body {
    margin: 0;
    padding: 0;
    overflow: hidden;
    background: var(--paper);
  }
  .card {
    position: relative;
    width: 1200px;
    height: 686px;
    overflow: hidden;
    background: var(--paper);
    font-family: "Roboto", Arial, sans-serif;
    color: var(--ink);
  }
  .logo-panel {
    position: absolute;
    left: 43px;
    top: 0;
    width: 427px;
    height: 200px;
    background: var(--navy);
    display: flex;
    align-items: center;
    justify-content: center;
    gap: 16px;
  }
  .logo-name {
    font-weight: 300;
    font-size: 72px;
    letter-spacing: 4px;
    color: var(--sky);
    line-height: 1;
  }
  .logo-dot {
    width: 26px;
    height: 26px;
    border-radius: 50%;
    background: var(--sky);
  }
  .brand-decoration {
    position: absolute;
    left: 722px;
    top: 0;
    width: 478px;
    height: 560px;
    background:
      radial-gradient(ellipse 62% 36% at 72% 68%, #1478c0 0%, #3d96d4 55%, rgba(255,255,255,0) 100%),
      radial-gradient(ellipse 78% 48% at 78% 22%, #8fa6da 0%, rgba(200,212,240,0.6) 60%, rgba(255,255,255,0) 100%);
  }
  .holder {
    position: absolute;
    left: 43px;
    top: 288px;
  }
  .holder-name {
    margin: 0;
    font-family: "Roboto Condensed", "Roboto", Arial, sans-serif;
    font-weight: 400;
    font-size: 41px;
    line-height: 1.1;
    color: var(--ink);
  }
  .holder-credentials {
    margin: 4px 0 0;
    font-weight: 400;
    font-size: 24px;
    color: var(--ink);
  }
  .contacts {
    position: absolute;
    left: 43px;
    top: 422px;
    margin: 0;
    padding: 0;
    list-style: none;
  }
  .contacts li {
    display: flex;
    align-items: center;
    height: 35px;
    font-size: 27px;
    color: var(--ink);
  }
  .contacts svg {
    width: 22px;
    height: 22px;
    margin-right: 14px;
    flex: none;
    fill: var(--icon);
  }
  .footer-band {
    position: absolute;
    left: 0;
    top: 617px;
    width: 1200px;
    height: 69px;
  }
  .slogan {
    position: absolute;
    left: 41px;
    top: 627px;
    margin: 0;
    font-family: "Kalam", cursive;
    font-weight: 300;
    font-size: 37px;
    line-height: 1.2;
    color: var(--slogan);
    letter-spacing: 0.5px;
    white-space: nowrap;
  }
</style>
</head>
<body>
<main class="card">
  <div class="logo-panel">
    <span class="logo-name">KelNova</span>
    <span class="logo-dot"></span>
  </div>

  <div class="brand-decoration" role="img" aria-label="Large blue brand globe decoration"></div>

  <section class="holder">
    <h1 class="holder-name">Daniel T Hoxley</h1>
    <p class="holder-credentials">BBus CA JP</p>
  </section>

  <ul class="contacts">
    <li>
      <svg viewBox="0 0 24 24" aria-hidden="true"><path d="M6.6 10.8a15.1 15.1 0 0 0 6.6 6.6l2.2-2.2c.3-.3.7-.4 1-.2 1.1.4 2.3.6 3.6.6.6 0 1 .4 1 1V20c0 .6-.4 1-1 1A17 17 0 0 1 3 4c0-.6.4-1 1-1h3.5c.6 0 1 .4 1 1 0 1.3.2 2.5.6 3.6.1.3 0 .7-.2 1z"/></svg>
      1800 531 908
    </li>
    <li>
      <svg viewBox="0 0 24 24" aria-hidden="true"><path d="M8 2h8a2 2 0 0 1 2 2v16a2 2 0 0 1-2 2H8a2 2 0 0 1-2-2V4a2 2 0 0 1 2-2zm0 3v11h8V5zm4 13a1 1 0 1 0 0 2 1 1 0 0 0 0-2z"/></svg>
      0412 385 714
    </li>
    <li>
      <svg viewBox="0 0 24 24" aria-hidden="true"><path d="M12 2a10 10 0 1 0 0 20 10 10 0 0 0 0-20zm6.9 9h-3a15 15 0 0 0-1.3-6A8 8 0 0 1 18.9 11zM12 4.1c.9 1.3 1.7 3.7 1.9 6.9h-3.8c.2-3.2 1-5.6 1.9-6.9zM9.4 5a15 15 0 0 0-1.3 6h-3A8 8 0 0 1 9.4 5zM5.1 13h3a15 15 0 0 0 1.3 6A8 8 0 0 1 5.1 13zm6.9 6.9c-.9-1.3-1.7-3.7-1.9-6.9h3.8c-.2 3.2-1 5.6-1.9 6.9zm2.6-.9a15 15 0 0 0 1.3-6h3a8 8 0 0 1-4.3 6z"/></svg>
      www.kelnovagroup.com.au
    </li>
    <li>
      <svg viewBox="0 0 24 24" aria-hidden="true"><path d="M2 5h20v14H2zm2 2v.4l8 5.2 8-5.2V7zm0 2.8V17h16V9.8l-8 5.2z"/></svg>
      admin@kelnovagroup.com.au
    </li>
  </ul>

  <svg class="footer-band" viewBox="0 0 1200 69" aria-hidden="true">
    <polygon points="0,0 795,0 727,69 0,69" fill="var(--navy)"/>
    <polygon points="816,0 1200,0 1200,69 748,69" fill="var(--brand-blue)"/>
  </svg>
  <p class="slogan">Smart Business Answers... That Deliver!</p>
</main>
</body>
</html>
```